back to back colour flier for child/teen psychology business

a5 size please, full colour.
modern, fresh.
appeals to parents.
with my logo which is attached, as is required text.

remember that we work with both children and teens, so any images would have to incorporate both groups.  Or have an image of a child as well as a teen........

```html
<!DOCTYPE html>
<html lang="en">
<head>
<meta charset="utf-8">
<title>Bright Paths Psychology and Education – Flyer</title>
<link rel="stylesheet" href="https://fonts.googleapis.com/css2?family=Arvo:ital,wght@1,700&family=Arimo:wght@400;700&display=swap">
<style>
  :root {
    --page-bg: #ececec;
    --sky: #2aa3dc;
    --cream: #fbeeb0;
    --ink-blue: #1f8fd0;
    --navy: #25378f;
    --orange: #e8692a;
    --grey-text: #6b6f75;
    --paper-top: #ffffff;
    --paper-bottom: #c9d1d9;
    --leaf: #5a8a2c;
  }
  * { box-sizing: border-box; margin: 0; padding: 0; }
  html, body { width: 1200px; height: 900px; overflow: hidden; background: var(--page-bg); }
  body { position: relative; font-family: "Arimo", Arial, sans-serif; }

  .flyer {
    position: absolute; left: 296px; top: 20px; width: 608px; height: 860px;
    background: linear-gradient(180deg, var(--paper-top) 45%, var(--paper-bottom) 100%);
    box-shadow: 0 6px 24px rgba(0,0,0,.18); overflow: hidden;
  }
  .flyer-shapes { position: absolute; inset: 0; }

  .intro-title {
    position: absolute; left: 36px; top: 34px; width: 390px;
    font-family: "Arvo", Georgia, serif; font-style: italic; font-weight: 700;
    font-size: 21px; line-height: 1.1; color: var(--cream);
  }
  .concern-list {
    position: absolute; left: 40px; top: 100px; width: 320px; list-style: none;
    color: #fff; font-size: 15px; line-height: 1.18;
  }
  .concern-list li { position: relative; padding-left: 18px; margin-bottom: 8px; }
  .concern-list li::before {
    content: ""; position: absolute; left: 0; top: 4px; width: 9px; height: 9px;
    background: #fff; border-radius: 2px;
  }

  .help-heading {
    position: absolute; left: 222px; top: 462px; width: 370px; text-align: center;
    font-family: "Arvo", Georgia, serif; font-style: italic; font-weight: 700;
    font-size: 19px; line-height: 1.15; color: var(--ink-blue);
  }

  .service-row { position: absolute; left: 36px; width: 536px; display: flex; gap: 12px; }
  .service-icon { flex: none; width: 34px; height: 34px; display: grid; place-items: center; }
  .service-text { font-size: 11px; line-height: 1.35; color: var(--grey-text); }
  .row-team { top: 524px; }
  .row-approach { top: 574px; }
  .row-cost { top: 630px; align-items: center; }
  .cost-pill {
    background: var(--navy); color: #dfe5ff; font-size: 11px; line-height: 1.3;
    padding: 6px 16px; border-radius: 0 16px 16px 0; width: 290px; margin-left: -12px;
  }

  .closing { position: absolute; left: 36px; top: 686px; width: 536px; font-size: 11px; line-height: 1.35; color: var(--grey-text); }
  .closing p + p { margin-top: 6px; }
  .closing strong { color: var(--navy); font-size: 14px; }

  .brand { position: absolute; left: 0; right: 0; top: 782px; display: flex; justify-content: center; align-items: center; gap: 10px; }
  .brand-mark { width: 30px; height: 30px; border-radius: 50%; background: var(--leaf); }
  .brand-text { color: var(--leaf); }
  .brand-name { font-size: 18px; font-weight: 700; letter-spacing: .5px; }
  .brand-tagline { font-size: 9.5px; font-weight: 700; }
  .brand-web { font-size: 9.5px; font-weight: 700; letter-spacing: 1px; }
</style>
</head>
<body>
  <article class="flyer">
    <svg class="flyer-shapes" width="608" height="860" viewBox="0 0 608 860">
      <defs>
        <linearGradient id="skyFill" x1="0" y1="0" x2="1" y2="1">
          <stop offset="0" stop-color="#1f95d5"/>
          <stop offset="1" stop-color="#3cb4e6"/>
        </linearGradient>
        <linearGradient id="kidsFill" x1="0" y1="0" x2="1" y2="1">
          <stop offset="0" stop-color="#c9785f"/>
          <stop offset=".5" stop-color="#8a5a7a"/>
          <stop offset="1" stop-color="#4b6fa8"/>
        </linearGradient>
        <linearGradient id="readerFill" x1="0" y1="0" x2="0" y2="1">
          <stop offset="0" stop-color="#d9b487"/>
          <stop offset=".5" stop-color="#e7eef5"/>
          <stop offset="1" stop-color="#2b2f3a"/>
        </linearGradient>
      </defs>
      <path d="M0 0 H608 V250 C520 262 470 318 410 330 H0 Z" fill="url(#skyFill)"/>
      <path d="M0 330 H410 C370 360 330 400 285 422 C245 442 180 452 100 455 H0 Z" fill="url(#kidsFill)" role="img" aria-label="Photo of a smiling group of children and teens"/>
      <rect x="388" y="62" width="190" height="365" rx="60" fill="url(#readerFill)" role="img" aria-label="Photo of a girl in glasses sitting cross-legged with an open book"/>
    </svg>

    <h1 class="intro-title">Many children and teens have times in life when they:</h1>
    <ul class="concern-list">
      <li>Feel worried, panicky and stressed.</li>
      <li>Have trouble managing their frustration</li>
      <li>Struggle with friendships and getting along with others</li>
      <li>Feel down, sad or hopeless</li>
      <li>Find school hard, or struggle to motivate themselves</li>
    </ul>

    <h2 class="help-heading">If you know or have a child/teen in this situation, then we can help</h2>

    <div class="service-row row-team">
      <span class="service-icon" style="background:var(--sky);border-radius:6px">
        <svg width="20" height="20" viewBox="0 0 20 20"><path d="M10 2 L19 10 H16 V18 H12 V13 H8 V18 H4 V10 H1 Z" fill="#fff"/></svg>
      </span>
      <p class="service-text">At Bright Paths Psychology and Education, we have eight experienced clinical psychologists who only work with children and teens and have worked with families in all kinds of situations.</p>
    </div>

    <div class="service-row row-approach">
      <span class="service-icon" style="background:var(--sky);border-radius:50%">
        <svg width="22" height="22" viewBox="0 0 22 22" fill="none" stroke="#fff" stroke-width="2.5"><circle cx="8" cy="12" r="4" stroke-dasharray="2 1.6"/><circle cx="16" cy="7" r="3" stroke-dasharray="2 1.4"/></svg>
      </span>
      <p class="service-text">We work with children/teens to build their resiliency, feel more positive, cope constructively with frustration and learn to get along with families and friends. We work with parents to help them know how to respond to and support the young person during this time.</p>
    </div>

    <div class="service-row row-cost">
      <span class="service-icon" style="background:var(--orange);border-radius:6px;width:40px;height:40px;position:relative;z-index:1">
        <svg width="20" height="24" viewBox="0 0 20 24"><text x="10" y="20" text-anchor="middle" font-family="Arimo, Arial, sans-serif" font-weight="700" font-size="22" fill="#fff">$</text></svg>
      </span>
      <p class="cost-pill">The majority of the cost of consultations are usually covered by HealthCover.</p>
    </div>

    <div class="closing">
      <p>We have child and teen friendly offices at Elmwood Park and Riverton, and have some after school hours consultations.</p>
      <p>If you would like more information <strong>call 8000 4521</strong>, or you can visit our website and also read a range of free articles about helping kids and young people through tough times.</p>
    </div>

    <div class="brand">
      <span class="brand-mark"></span>
      <div class="brand-text">
        <div class="brand-name">BRIGHT PATHS PSYCHOLOGY AND EDUCATION</div>
        <div class="brand-tagline">Helping kids &amp; teens learn life skills &amp; manage tough times</div>
        <div class="brand-web">www.brightpaths.net.au</div>
      </div>
    </div>
  </article>
</body>
</html>
```